Business Card Design

We need two business cards - same design but with two different people's details.

We are a new start-up online cleaning business that allows people to book and pay for a quality home cleaner online.

We would like a professional yet overly formal style of business card.

Target Market(s)

18 - 65+ professionals

Industry/Entity Type

Business

Contact Information for Business Card

We would like two business cards but with the same design, the details are below:

Peter Valdoro
Director and Co-Founder
ph: 0421 573 916
Suite 3C, Level 4
517 Harwood Road
Belmira NSW 2089
peter@tidlo.com.au

_______________________________________________________

Evangelia Valdoro
Director and Co-Founder
ph: 0432 915047
Suite 3C, Level 4
517 Harwood Road
Belmira NSW 2089
evangelia@tidlo.com.au

Requirements
Must have
• although our style guide refers to orange and red, please stick to the blue/black/grey that is in the style guide.

also on the back of the card we would like the logo with our tag line which is on page 12 of the style guide.
Should not have
• no pictures of mops, cleaners etc

```html
<!DOCTYPE html>
<html lang="en">
<head>
<meta charset="utf-8">
<title>Tidlo Business Cards</title>
<link rel="stylesheet" href="https://fonts.googleapis.com/css2?family=Lato:wght@300;400;700;900&display=swap">
<style>
  :root {
    --backdrop: #e4e4e2;
    --card-dark: #1e1e1f;
    --card-mid: #3a3a3c;
    --card-edge: #111112;
    --brand-blue: #0aa0dc;
    --band-white: #f2f2f2;
    --ink-dark: #1c1c1c;
    --ink-light: #ffffff;
    --ink-muted: #a9abad;
    --rule: #5a5b5d;
    --mark-grey: #b9bbbd;
  }
  * { box-sizing: border-box; margin: 0; padding: 0; }
  html, body {
    width: 1200px; height: 900px; overflow: hidden;
    background: var(--backdrop);
    font-family: "Lato", Arial, sans-serif;
  }
  .canvas { position: relative; width: 1200px; height: 900px; }

  .card {
    position: absolute;
    width: 520px; height: 300px;
    border-radius: 18px;
    overflow: hidden;
    background: radial-gradient(ellipse at 70% 20%, var(--card-mid) 0%, var(--card-dark) 65%);
    box-shadow: 0 10px 30px rgba(0,0,0,.25);
  }
  .card--front { left: 150px; top: 100px; }
  .card--back { left: 530px; top: 500px; }

  /* Front */
  .front__edge {
    position: absolute; left: 0; top: 0; bottom: 0; width: 36px;
    background: var(--card-edge);
  }
  .front__blue {
    position: absolute; left: 36px; top: 0; bottom: 0; width: 250px;
    background: var(--brand-blue);
  }
  .front__band {
    position: absolute; left: 0; right: 0; top: 150px; height: 86px;
    background: linear-gradient(180deg, #ffffff, var(--band-white) 60%, #dcdcdc);
    display: flex; align-items: center; padding-left: 52px; gap: 14px;
  }
  .brand__dot {
    width: 46px; height: 46px; border-radius: 50%;
    background: var(--brand-blue); flex: none;
  }
  .brand__name {
    font-weight: 900; font-size: 40px; line-height: 1;
    color: var(--ink-dark); letter-spacing: .5px;
  }
  .brand__tagline {
    font-weight: 300; font-size: 12px; color: var(--ink-dark);
    margin-top: 4px; letter-spacing: .3px;
  }

  /* Back */
  .back__edge {
    position: absolute; left: 0; top: 0; bottom: 0; width: 34px;
    background: var(--card-edge);
  }
  .back__blue {
    position: absolute; left: 34px; top: 0; bottom: 0; width: 190px;
    background: var(--brand-blue);
    display: flex; flex-direction: column; align-items: center; justify-content: center; gap: 12px;
  }
  .back__mark {
    width: 96px; height: 96px; border-radius: 50%;
    background: var(--mark-grey);
  }
  .back__mark-name {
    font-weight: 900; font-size: 30px; color: var(--mark-grey); line-height: 1;
  }
  .back__details {
    position: absolute; left: 248px; right: 26px; top: 40px;
    color: var(--ink-light);
  }
  .person__name {
    font-weight: 700; font-size: 15px; letter-spacing: 1px; text-transform: uppercase;
  }
  .person__role {
    font-weight: 400; font-size: 12px; color: var(--ink-muted); margin-top: 1px;
  }
  .rule { height: 1px; background: var(--rule); margin: 10px 0 14px; }
  .address { font-size: 12px; line-height: 1.45; color: var(--ink-muted); }
  .contact {
    display: flex; align-items: center; gap: 12px;
    font-size: 12px; color: var(--ink-muted); margin-bottom: 16px;
  }
  .contact svg { width: 13px; height: 13px; fill: var(--ink-muted); flex: none; }
</style>
</head>
<body>
<main class="canvas">

  <section class="card card--front" aria-label="Business card front">
    <div class="front__edge"></div>
    <div class="front__blue"></div>
    <div class="front__band">
      <span class="brand__dot"></span>
      <div class="brand">
        <div class="brand__name">Tidlo</div>
        <div class="brand__tagline">Save time. Book a quality cleaner online.</div>
      </div>
    </div>
  </section>

  <section class="card card--back" aria-label="Business card back">
    <div class="back__edge"></div>
    <div class="back__blue">
      <span class="back__mark"></span>
      <span class="back__mark-name">Tidlo</span>
    </div>
    <div class="back__details">
      <div class="person__name">Peter Valdoro</div>
      <div class="person__role">Director and Co-Founder</div>
      <div class="rule"></div>
      <p class="address">Suite 3C, Level 4 517 Harwood Road Belmira<br>NSW 2089</p>
      <div class="rule"></div>
      <div class="contact">
        <svg viewBox="0 0 16 16" aria-hidden="true"><path d="M2 4c0-1 1-2 2-2h8c1 0 2 1 2 2v1h-3V4H5v1H2zM3 7l2-2h6l2 2v6H3zM8 8a2 2 0 1 0 0 4 2 2 0 0 0 0-4z"/></svg>
        <span>0421 573 916</span>
      </div>
      <div class="contact">
        <svg viewBox="0 0 16 16" aria-hidden="true"><path d="M1 3h14v10H1zM2 4v1l6 4 6-4V4L8 8z"/></svg>
        <span>peter@tidlo.com.au</span>
      </div>
    </div>
  </section>

</main>
</body>
</html>
```